Webdesign für Bedrucken Papiertaschen, Schildern etc.
Zielgruppe
Wir bedrucken Papiertaschen, Papierbeutel, Laternen, Aluplaketten, Schilder, etc. und lasern Hundemarken. Zielgruppen von Privat bis Geschäftskunden
Aufgabenstellung
Der Shop sollte ein einfacher und kostengünstiger 'printfeld'-shop werden. Wo die Kunden anhand von einem Editor Ihre Logos oder Druckvorlagen selber hochladen und/oder gestalten könne. Bisher haben die Kunden eifach ihre Bidldatei per E-Mail geschickt und wir haben diese dann weiter verarbeit.
Der Shop sollte, wenn möglich, günstig im Unterhalt sein, da wir nicht abschätzen können, wie gut diese laufen wird.
Wir haben wie 3 Bereich: 1. Papierbeutel/Taschen / 2. Stallplaketten (für z.B. Pferdesport) / 3. Diverses (Wie z.B. die Laternen, Schilder, Hundemarken, etc.)
Es würde sich um eine separate Webseite handeln. Daher ist bei Design freie Hand, eifach und klar... auch für nicht so ambitionierte Privatkunden oder kleine Unternehmen.

```html
<!DOCTYPE html>
<html lang="de">
<head>
<meta charset="utf-8">
<title>printfeld – Produkte</title>
<link rel="stylesheet" href="https://fonts.googleapis.com/css2?family=Inter:wght@400;500;600;700;800&display=swap">
<style>
:root{
  --stage:#c0c0c0;
  --page:#f6f7f9;
  --white:#ffffff;
  --ink:#0d1321;
  --muted:#5b6170;
  --line:#e6e8ec;
  --lime:#b8ec3c;
  --lime-text:#a6d92c;
  --navy:#0c1426;
}
*{box-sizing:border-box;margin:0;padding:0}
html,body{width:699px;height:1200px;overflow:hidden}
body{background:var(--stage);font-family:"Inter",sans-serif;color:var(--ink);position:relative}
.page{position:absolute;left:53px;top:47px;width:591px;height:1100px;background:var(--page);overflow:hidden}
.nav{position:absolute;left:50px;top:10px;width:490px;height:21px;background:var(--white);border-radius:11px;box-shadow:0 1px 4px rgba(0,0,0,.05);display:flex;align-items:center;padding:0 5px 0 8px}
.brand{font-weight:700;font-size:12.5px;letter-spacing:-.3px;display:flex;align-items:center;gap:4px}
.brand .dot{width:6px;height:6px;background:var(--lime);border-radius:50%}
.nav-links{margin-left:auto;display:flex;gap:11px;font-size:5.6px;font-weight:500;align-items:center}
.nav-links .active{border-bottom:1px solid var(--lime);padding-bottom:1px}
.nav-search{width:12px;height:12px;border:1px solid var(--line);border-radius:50%;margin-left:14px;display:flex;align-items:center;justify-content:center}
.btn{background:var(--ink);color:var(--white);border-radius:8px;font-weight:600;display:inline-flex;align-items:center;justify-content:center;gap:3px}
.nav .btn{margin-left:6px;height:14px;padding:0 8px;font-size:5.6px}
.crumbs{position:absolute;left:53px;top:52px;font-size:4.6px;color:var(--muted)}
.crumbs b{color:var(--ink);font-weight:500}
.eyebrow{position:absolute;left:53px;top:67px;font-size:4.4px;font-weight:700;letter-spacing:1.4px;color:var(--lime-text)}
h1{position:absolute;left:53px;top:77px;font-size:23.5px;line-height:24px;font-weight:800;letter-spacing:-.9px}
.search{position:absolute;left:343px;top:105px;width:195px;height:19px;background:var(--white);border:1px solid var(--line);border-radius:10px;display:flex;align-items:center;padding:0 2px 0 7px;font-size:5.4px;color:#8a8f9a;gap:5px}
.search .btn{margin-left:auto;height:13px;padding:0 6px;font-size:4.8px}
.filterbar{position:absolute;left:0;top:150px;width:591px;height:26px;background:var(--white);border-top:1px solid var(--line);border-bottom:1px solid var(--line);display:flex;align-items:center;padding:0 53px}
.chip{height:13px;border:1px solid var(--line);border-radius:7px;font-size:5.5px;font-weight:500;display:flex;align-items:center;gap:4px;padding:0 6px;margin-right:4px;background:var(--white)}
.chip span{font-size:3.8px;background:#eef0f3;border-radius:4px;padding:1px 2px}
.chip.on{background:var(--ink);color:var(--white);border-color:var(--ink)}
.chip.on span{background:#3a4152;color:var(--white)}
.sort{margin-left:auto;font-size:4.6px;color:var(--muted)}
.sort b{color:var(--ink);margin-left:3px}
.grid{position:absolute;left:53px;top:195px;width:486px;display:grid;grid-template-columns:repeat(3,156px);gap:8px 9px}
.card{height:190px;background:var(--white);border:1px solid var(--line);border-radius:8px;overflow:hidden;position:relative}
.art{height:125px;position:relative}
.tag{position:absolute;left:5px;top:5px;background:var(--white);border-radius:5px;font-size:3.9px;font-weight:600;padding:1.5px 3px}
.flags{position:absolute;right:5px;top:5px;display:flex;flex-direction:column;align-items:flex-end;gap:2px}
.flag{font-size:3.9px;font-weight:600;border-radius:5px;padding:1.5px 4px;background:var(--ink);color:var(--white)}
.flag.up{background:var(--lime);color:var(--ink)}
.info{padding:10px 10px 0}
.info h3{font-size:8px;font-weight:700;letter-spacing:-.2px}
.info p{font-size:5.4px;color:var(--muted);margin-top:4px}
.buy{position:absolute;left:10px;right:10px;bottom:11px;display:flex;align-items:flex-end}
.price small{display:block;font-size:3.6px;font-weight:700;color:var(--muted);letter-spacing:.4px}
.price strong{font-size:7.6px;font-weight:700}
.price em{font-style:normal;font-size:4.4px;color:var(--muted)}
.buy .btn{margin-left:auto;height:14px;width:43px;font-size:5px}
.cta{position:absolute;left:53px;top:807px;width:486px;height:112px;background:var(--lime);border-radius:10px;text-align:center;padding-top:22px}
.cta h2{font-size:15px;font-weight:800;letter-spacing:-.5px}
.cta p{font-size:5.9px;line-height:9.3px;color:#2b3320;margin:6px auto 0;width:220px}
.cta .btn{height:19px;padding:0 10px;font-size:5.8px;margin-top:9px;border-radius:10px}
.footer{position:absolute;left:0;top:948px;width:591px;height:152px;background:var(--navy);color:#b7bcc8}
.footer .brand{position:absolute;left:53px;top:25px;color:var(--white);font-size:13px}
.about{position:absolute;left:53px;top:50px;width:145px;font-size:5.3px;line-height:7.8px}
.footer .lime-btn{position:absolute;left:53px;top:80px;height:16px;padding:0 8px;border-radius:8px;background:var(--lime);color:var(--ink);font-size:5.6px;font-weight:600;display:flex;align-items:center;gap:3px}
.col{position:absolute;top:29px;font-size:5.3px}
.col h4{color:var(--white);font-size:5.5px;font-weight:600;margin-bottom:9px}
.col li{list-style:none;margin-bottom:6.5px}
.contact li{display:flex;gap:4px;align-items:flex-start}
.bottom{position:absolute;left:53px;right:53px;top:124px;border-top:1px solid #222a3b;padding-top:10px;display:flex;font-size:4.5px;color:#8a90a0}
.bottom nav{margin-left:auto;display:flex;gap:10px}
</style>
</head>
<body>
<div class="page">
  <header class="nav">
    <div class="brand">printfeld<span class="dot"></span></div>
    <nav class="nav-links">
      <span class="active">Produkte</span><span>Editor</span><span>Beispiel</span><span>Kontakt</span>
    </nav>
    <span class="nav-search"><svg width="6" height="6" viewBox="0 0 12 12" fill="none" stroke="#0d1321" stroke-width="1.5"><circle cx="5" cy="5" r="3.5"/><path d="M8 8l3 3"/></svg></span>
    <span class="btn">Editor öffnen ↗</span>
  </header>

  <div class="crumbs">Home &nbsp;›&nbsp; <b>Produkte</b></div>
  <div class="eyebrow">KATALOG</div>
  <h1>Was möchten Sie<br>heute gestalten?</h1>
  <div class="search">
    <svg width="6" height="6" viewBox="0 0 12 12" fill="none" stroke="#5b6170" stroke-width="1.5"><circle cx="5" cy="5" r="3.5"/><path d="M8 8l3 3"/></svg>
    Produkt suchen...
    <span class="btn">☰ Filter</span>
  </div>

  <div class="filterbar">
    <span class="chip on">Alle <span>18</span></span>
    <span class="chip">Papierbeutel &amp; Taschen <span>6</span></span>
    <span class="chip">Stallplaketten <span>5</span></span>
    <span class="chip">Diverses <span>7</span></span>
    <span class="sort">Sortieren: <b>Beliebt ↓</b></span>
  </div>

  <main class="grid">
    <article class="card">
      <div class="art" role="img" aria-label="Standbodenbeutel aus Kraftpapier mit Logofeld" style="background:linear-gradient(135deg,#fff1c4,#fdd9a0)"><span class="tag">Verpackung</span><div class="flags"><span class="flag">Editor</span><span class="flag up">Upload</span></div></div>
      <div class="info"><h3>Standbodenbeutel</h3><p>Kraftpapier · 1- oder 2-seitig · mit/ohne Fenster</p></div>
      <div class="buy"><div class="price"><small>AB</small><strong>CHF 1.20</strong><em>/ Stk</em></div><span class="btn">Gestalten ↗</span></div>
    </article>
    <article class="card">
      <div class="art" role="img" aria-label="Weisse Papiertasche mit Markendruck" style="background:linear-gradient(135deg,#fbf8ee,#faf0c6)"><span class="tag">Verpackung</span><div class="flags"><span class="flag">Editor</span><span class="flag up">Upload</span></div></div>
      <div class="info"><h3>Papiertasche</h3><p>Tragetasche mit Logodruck, mehrere Grössen</p></div>
      <div class="buy"><div class="price"><small>AB</small><strong>CHF 1.90</strong><em>/ Stk</em></div><span class="btn">Gestalten ↗</span></div>
    </article>
    <article class="card">
      <div class="art" role="img" aria-label="Ovale rosa Stallplakette mit Pferdename" style="background:linear-gradient(135deg,#fde0e6,#f9c5de)"><span class="tag">Pferdesport</span><div class="flags"><span class="flag">Editor</span></div></div>
      <div class="info"><h3>Stallplakette Oval</h3><p>Holz oder Aluminium · Wunschtext</p></div>
      <div class="buy"><div class="price"><small>AB</small><strong>CHF 24.00</strong></div><span class="btn">Gestalten ↗</span></div>
    </article>
    <article class="card">
      <div class="art" role="img" aria-label="Eckige dunkle Stallplakette mit Gravur" style="background:linear-gradient(135deg,#fbe0ef,#fdd3dd)"><span class="tag">Pferdesport</span><div class="flags"><span class="flag">Editor</span><span class="flag up">Upload</span></div></div>
      <div class="info"><h3>Stallplakette Eckig</h3><p>Aluminium · wetterfest · 20×30 cm</p></div>
      <div class="buy"><div class="price"><small>AB</small><strong>CHF 32.00</strong></div><span class="btn">Gestalten ↗</span></div>
    </article>
    <article class="card">
      <div class="art" role="img" aria-label="Runde Hundemarke aus Edelstahl" style="background:linear-gradient(135deg,#d7f1fb,#a8eefa)"><span class="tag">Diverses</span><div class="flags"><span class="flag">Editor</span></div></div>
      <div class="info"><h3>Hundemarke</h3><p>Edelstahl, Aluminium · mit Gravur</p></div>
      <div class="buy"><div class="price"><small>AB</small><strong>CHF 14.90</strong></div><span class="btn">Gestalten ↗</span></div>
    </article>
    <article class="card">
      <div class="art" role="img" aria-label="Kleine schwarze Laterne mit Wunschmotiv" style="background:linear-gradient(135deg,#e4e3fa,#c9cffb)"><span class="tag">Diverses</span><div class="flags"><span class="flag">Editor</span><span class="flag up">Upload</span></div></div>
      <div class="info"><h3>Laterne klein</h3><p>Mit Wunschmotiv · schwarz oder weiss</p></div>
      <div class="buy"><div class="price"><small>AB</small><strong>CHF 49.90</strong></div><span class="btn">Gestalten ↗</span></div>
    </article>
    <article class="card">
      <div class="art" role="img" aria-label="Grosse schwarze Laterne, beidseitig bedruckt" style="background:linear-gradient(135deg,#dbe4fb,#c2dbfb)"><span class="tag">Diverses</span><div class="flags"><span class="flag">Editor</span></div></div>
      <div class="info"><h3>Laterne gross</h3><p>Beidseitig bedruckbar · LED-tauglich</p></div>
      <div class="buy"><div class="price"><small>AB</small><strong>CHF 79.00</strong></div><span class="btn">Gestalten ↗</span></div>
    </article>
    <article class="card">
      <div class="art" role="img" aria-label="Dunkle Aluplakette mit Beschriftung" style="background:linear-gradient(135deg,#f1f2f4,#e4e4e8)"><span class="tag">Diverses</span><div class="flags"><span class="flag up">Upload</span></div></div>
      <div class="info"><h3>Aluplakette</h3><p>Wetterfest · individuelle Grössen</p></div>
      <div class="buy"><div class="price"><small>AB</small><strong>Anfrage</strong></div><span class="btn">Gestalten ↗</span></div>
    </article>
    <article class="card">
      <div class="art" role="img" aria-label="Gelber Geschenkbeutel mit Logofeld" style="background:linear-gradient(135deg,#fff7d2,#fdf0b8)"><span class="tag">Verpackung</span><div class="flags"><span class="flag">Editor</span></div></div>
      <div class="info"><h3>Geschenkbeutel</h3><p>Klein · Kraftpapier · ideal für Events</p></div>
      <div class="buy"><div class="price"><small>AB</small><strong>CHF 0.90</strong><em>/ Stk</em></div><span class="btn">Gestalten ↗</span></div>
    </article>
  </main>

  <section class="cta">
    <h2>Produkt nicht dabei?</h2>
    <p>Wir realisieren auch individuelle Druckprodukte. Senden Sie uns eine Anfrage mit Ihren Anforderungen.</p>
    <span class="btn">Anfrage senden ↗</span>
  </section>

  <footer class="footer">
    <div class="brand">printfeld<span class="dot"></span></div>
    <p class="about">Druckprodukte online gestalten — Editor, Upload und persönliche Datenprüfung. Lokale Produktion in der Schweiz.</p>
    <span class="lime-btn">Editor öffnen ↗</span>
    <div class="col" style="left:254px"><h4>Produkte</h4><ul><li>Papierbeutel</li><li>Stallplaketten</li><li>Laternen</li><li>Hundemarken</li><li>Alle Produkte</li></ul></div>
    <div class="col" style="left:322px"><h4>Service</h4><ul><li>Editor öffnen</li><li>Datei hochladen</li><li>Datenprüfung</li><li>Versand</li><li>Kontakt</li></ul></div>
    <div class="col" style="left:390px"><h4>Unternehmen</h4><ul><li>Über uns</li><li>Druckpartner</li><li>Nachhaltigkeit</li><li>Impressum</li><li>Datenschutz</li></ul></div>
    <div class="col contact" style="left:464px"><h4>Kontakt</h4><ul>
      <li><svg width="6" height="6" viewBox="0 0 12 12" fill="none" stroke="#b8ec3c" stroke-width="1.3"><rect x="1" y="2.5" width="10" height="7" rx="1"/><path d="M1 3l5 4 5-4"/></svg>hallo@printfeld.ch</li>
      <li><svg width="6" height="6" viewBox="0 0 12 12" fill="none" stroke="#b8ec3c" stroke-width="1.3"><path d="M2 1.5h2.5l1 3-1.5 1a7 7 0 0 0 2.5 2.5l1-1.5 3 1V10a1 1 0 0 1-1 1A9 9 0 0 1 1 2.5a1 1 0 0 1 1-1z"/></svg>+41 44 555 01 20</li>
      <li><svg width="6" height="6" viewBox="0 0 12 12" fill="none" stroke="#b8ec3c" stroke-width="1.3"><path d="M6 11s4-4 4-6.5a4 4 0 0 0-8 0C2 7 6 11 6 11z"/><circle cx="6" cy="4.5" r="1.3"/></svg><span>Seeweg 12<br>8001 Zürich</span></li>
    </ul></div>
    <div class="bottom"><span>© 2026 printfeld. Alle Rechte vorbehalten.</span><nav><span>Impressum</span><span>Datenschutz</span><span>AGB</span></nav></div>
  </footer>
</div>
</body>
</html>
```